Water Damage? Call Us!!

We are an established water damage mitigation company opening a storm chasing division. We will need the flyer to express urgency to call for water damage structural drying and demolition. I have attached our logo in various formats.

Check out our website for some ideas of what we do. www.parklinerestoration.com

Include:

Parkline Restoration, LLC
Office@ParklineRestoration.com
www.parklinerestoration.com
877-HELP-NOW
877-435-7669

I don't want to have our locations on there.

Target Market(s)

When someone has water damage to their home or business, we remove the wet material and then use fans and dehumidifiers to remove the moisture from the structure. We are like a Kelvora, but better. Lol

Colors

Designer to choose colors to be used in the design.

Requirements
Must have
• I have included various certification logos to use.
• Water damage must be the main focal point.
• We need to call them to action by calling us to dry their property. We will be dropping these flyers off in damaged areas.
• Trained in Drying Science by the NBRTA
• We handle Residential, Commercial, Hotels, Multi-Family.
• We specialize in Insurance Claims.
• We can bill your insurance company directly.
• Our Services include:
• Water Extraction/Muck Out
• Deconstruction of Damaged Materials
• Structural Drying
• Anti-Microbial Application
• Roofing
Nice to have
• It would be nice to have some thermal images of wet areas
Should not have
• Not looking for a fun flyer. These potential clients have suffered from devastation and we are looking to help them by getting their home or business back to normal.

```html
<!DOCTYPE html>
<html lang="en">
<head>
<meta charset="utf-8">
<title>Water Damage Restoration – Parkline Restoration</title>
<link href="https://fonts.googleapis.com/css2?family=Oswald:wght@400;500;700&display=swap" rel="stylesheet">
<style>
  :root{
    --navy:#2e3192;
    --red:#e30d0f;
    --white:#ffffff;
    --photo-sky:#8fa3b4;
    --photo-blue:#2f8fd8;
    --photo-grey:#b8b6b0;
    --badge-grey:#c9c9c9;
  }
  *{box-sizing:border-box;margin:0;padding:0}
  html,body{width:938px;height:1200px;overflow:hidden;background:var(--white)}
  .flyer{position:relative;width:938px;height:1200px;background:var(--navy);font-family:"Oswald",sans-serif;color:var(--white);overflow:hidden}
  .hero-photo{position:absolute;left:0;top:0;width:938px;height:520px;
    background:linear-gradient(180deg,#6b7a6a 0%,#8a7f72 35%,var(--photo-blue) 55%,var(--photo-grey) 100%)}
  .roofline{position:absolute;left:0;top:0;width:938px;height:1200px}
  .brand-flag{position:absolute;left:672px;top:0;width:214px;height:185px}
  .brand-name{position:absolute;left:672px;top:52px;width:214px;display:flex;align-items:center;justify-content:center;gap:8px;
    color:var(--navy);font-weight:700;font-size:21px;line-height:1.05;text-transform:uppercase;text-align:left}
  .brand-name .dot{width:16px;height:16px;border-radius:50%;background:var(--red);flex:none}
  .headline{position:absolute;left:0;width:938px;text-align:center;font-weight:700;text-transform:uppercase;
    letter-spacing:3px;line-height:1;text-shadow:0 0 2px #111,2px 2px 0 #111}
  .headline.line1{top:500px;font-size:82px}
  .headline.line2{top:578px;font-size:82px}
  .service{position:absolute;left:42px;width:421px;height:113px;display:flex}
  .service-label{width:139px;background:var(--red);padding:0 12px;display:flex;flex-direction:column;justify-content:center;
    font-size:14px;font-weight:500;line-height:1.4;text-transform:uppercase}
  .service-photo{flex:1}
  .svc1{top:669px}.svc2{top:792px}.svc3{top:915px}
  .svc1 .service-photo{background:linear-gradient(135deg,#e9e4da,#8d877c 60%,#4b4a47)}
  .svc2 .service-photo{background:linear-gradient(135deg,#d8d2c4,#8a6a4e 55%,#3e3a34)}
  .svc3 .service-photo{background:linear-gradient(180deg,#e6e2da,#b5ada0 60%,#6f9b6a)}
  .why{position:absolute;left:493px;top:668px}
  .why h2{font-size:34px;font-weight:500;line-height:1}
  .why ul{list-style:none;margin-top:14px}
  .why li{display:flex;align-items:center;gap:6px;height:27.2px;font-size:17px;text-transform:uppercase;letter-spacing:.4px}
  .why li svg{flex:none}
  .cta{position:absolute;left:493px;top:947px;width:402px;height:78px;border-top:3px solid var(--white);border-bottom:3px solid var(--white);
    padding-top:4px;font-size:33px;font-weight:500;line-height:1.03;text-transform:uppercase}
  .promise{position:absolute;left:0;top:1047px;width:938px;text-align:center;font-size:17px;line-height:1.45;text-transform:uppercase;letter-spacing:.3px}
  .cert-strip{position:absolute;left:0;top:1108px;width:938px;height:75px;background:var(--white);
    display:flex;align-items:center;justify-content:space-around;padding:0 30px}
  .cert{background:var(--badge-grey)}
  .cert.wide{width:106px;height:40px;border-radius:4px}
  .cert.round{width:50px;height:50px;border-radius:50%}
  .cert.square{width:52px;height:44px}
  .base-band{position:absolute;left:0;top:1183px;width:938px;height:17px;background:var(--red)}
</style>
</head>
<body>
<main class="flyer">
  <div class="hero-photo" role="img" aria-label="Technician standing behind long rows of stacked blue air movers on a driveway in front of a brick house"></div>

  <svg class="roofline" viewBox="0 0 938 1200" aria-hidden="true">
    <polygon points="0,501 469,407 938,501 938,1108 0,1108" fill="var(--navy)"/>
    <polygon points="0,525 469,432 938,525 938,560 469,467 0,560" fill="var(--red)"/>
  </svg>

  <svg class="brand-flag" viewBox="0 0 214 185" aria-hidden="true">
    <polygon points="0,0 214,0 214,185 107,160 0,185" fill="var(--white)"/>
  </svg>
  <div class="brand-name"><span class="dot"></span><span>Parkline<br>Restoration</span></div>

  <h1 class="headline line1">Water</h1>
  <div class="headline line2">Damage Restoration</div>

  <section class="service svc1">
    <div class="service-label"><span>Water Extraction</span><span>Muck Out</span></div>
    <div class="service-photo" role="img" aria-label="Worker extracting standing water from a flooded hallway with an orange hose"></div>
  </section>
  <section class="service svc2">
    <div class="service-label"><span>Deconstruction</span><span>of Damaged</span><span>Materials</span></div>
    <div class="service-photo" role="img" aria-label="Crew removing wet drywall down to the studs"></div>
  </section>
  <section class="service svc3">
    <div class="service-label"><span>Structural Drying</span><span>Anti-Microbial</span><span>Application</span></div>
    <div class="service-photo" role="img" aria-label="Room with air movers and a dehumidifier drying the structure"></div>
  </section>

  <section class="why">
    <h2>WHY US?</h2>
    <ul>
      <li><svg width="14" height="12" viewBox="0 0 14 12"><path d="M1 6 L5 10 L13 1" fill="none" stroke="var(--red)" stroke-width="2.4"/></svg>Trained in structural drying science</li>
      <li><svg width="14" height="12" viewBox="0 0 14 12"><path d="M1 6 L5 10 L13 1" fill="none" stroke="var(--red)" stroke-width="2.4"/></svg>Trained insurance adjusters</li>
      <li><svg width="14" height="12" viewBox="0 0 14 12"><path d="M1 6 L5 10 L13 1" fill="none" stroke="var(--red)" stroke-width="2.4"/></svg>Trained in building sciences</li>
      <li><svg width="14" height="12" viewBox="0 0 14 12"><path d="M1 6 L5 10 L13 1" fill="none" stroke="var(--red)" stroke-width="2.4"/></svg>Can bill your insurance company directly</li>
      <li><svg width="14" height="12" viewBox="0 0 14 12"><path d="M1 6 L5 10 L13 1" fill="none" stroke="var(--red)" stroke-width="2.4"/></svg>3 decades of general contracting experience</li>
      <li><svg width="14" height="12" viewBox="0 0 14 12"><path d="M1 6 L5 10 L13 1" fill="none" stroke="var(--red)" stroke-width="2.4"/></svg>Able to handle your complete project turnkey</li>
      <li><svg width="14" height="12" viewBox="0 0 14 12"><path d="M1 6 L5 10 L13 1" fill="none" stroke="var(--red)" stroke-width="2.4"/></svg>Detailed documentation of your property loss</li>
      <li><svg width="14" height="12" viewBox="0 0 14 12"><path d="M1 6 L5 10 L13 1" fill="none" stroke="var(--red)" stroke-width="2.4"/></svg>Residential, commercial, hotels, multi-family</li>
    </ul>
  </section>

  <div class="cta">Request a visit<br>Call us at 877-HELP-NOW</div>

  <p class="promise">The trained staff at Parkline Restoration will meet your insurance adjuster on site and provide<br>detailed documentation of your property and the loss.</p>

  <div class="cert-strip" aria-label="Certifications">
    <span class="cert wide"></span>
    <span class="cert round"></span>
    <span class="cert wide"></span>
    <span class="cert round"></span>
    <span class="cert wide"></span>
    <span class="cert square"></span>
    <span class="cert wide"></span>
    <span class="cert round"></span>
    <span class="cert round"></span>
  </div>
  <div class="base-band"></div>
</main>
</body>
</html>
```